Business Card Design

We are a business based in Sydney repairing and restoring timber windows. We mainly cater to residential home owners although sometimes work with larger building companies. We do a lot of work in heritage buildings though also cater to modern windows.
Our Logo is Black and Gold and were thinking of using a white card with only these two colours although we are open to any design suggestions. Check out our website for ideas.
Front of Card
Contact Information, Website & Business Name
Back of Card
Business Logo, website?
Target Market(s)
Home Owners
Industry/Entity Type
Residential
Contact Information for Business Card
Casement Craft Renewals
Owen Castell
0457 302 689
owen@casementcraftrenewals.com
www.casementcraftrenewals.com
Look and feel

```html
<!DOCTYPE html>
<html lang="en">
<head>
<meta charset="utf-8">
<title>Casement Craft Renewals – Business Cards</title>
<link href="https://fonts.googleapis.com/css2?family=Source+Sans+3:wght@400;600&display=swap" rel="stylesheet">
<style>
  :root {
    --backdrop: #e6e6e4;
    --card-white: #f7f7f6;
    --frame-light: #ffffff;
    --frame-shade: #d9d9d7;
    --ink-dark: #3b3a37;
    --ink-text: #f4f2ec;
    --gold: #9a7a2c;
    --mark-ink: #6b5416;
    --room-warm: #cbb48e;
    --room-cool: #bdbab3;
    --room-light: #ecebe7;
  }
  * { box-sizing: border-box; margin: 0; padding: 0; }
  html, body { width: 1200px; height: 900px; overflow: hidden; }
  body {
    background: var(--backdrop);
    font-family: "Source Sans 3", "Myriad Pro", Arial, sans-serif;
    position: relative;
  }
  .card {
    position: absolute;
    width: 540px;
    height: 310px;
    background: var(--card-white);
    box-shadow: 0 6px 18px rgba(0,0,0,.18);
  }

  /* Back of card */
  .card--back { left: 50px; top: 120px; padding: 20px; }
  .bevel-frame {
    width: 100%; height: 100%;
    padding: 12px;
    background: var(--frame-light);
    border: 1px solid var(--frame-shade);
    box-shadow: inset 0 0 0 4px var(--frame-light), inset 0 0 0 5px var(--frame-shade);
  }
  .room-view {
    position: relative;
    width: 100%; height: 100%;
    background: linear-gradient(100deg, var(--room-light) 0%, var(--room-cool) 35%, var(--room-warm) 60%, var(--room-light) 100%);
    box-shadow: inset 0 0 0 1px var(--frame-shade);
  }
  .room-view .mark { position: absolute; left: 50%; top: 22px; transform: translateX(-50%); }
  .room-view .web-strip { position: absolute; left: 50%; top: 146px; transform: translateX(-50%); }
  .contact-bar {
    position: absolute; left: 14px; right: 14px; bottom: 14px;
    background: var(--ink-dark);
    color: var(--ink-text);
    text-align: center;
    font-size: 15px; line-height: 19px;
    padding: 9px 8px;
  }

  /* Brand mark: name in a plain circle */
  .mark {
    width: 118px; height: 118px;
    border-radius: 50%;
    background: var(--frame-light);
    border: 1px solid var(--frame-shade);
    display: flex; align-items: center; justify-content: center;
    text-align: center;
    color: var(--mark-ink);
    font-weight: 600; font-size: 17px; line-height: 19px;
  }
  .web-strip {
    background: var(--ink-dark);
    color: var(--ink-text);
    font-size: 10.5px;
    padding: 2px 7px;
    white-space: nowrap;
  }

  /* Front of card */
  .card--front { left: 610px; top: 470px; }
  .card--front .mark { position: absolute; left: 92px; top: 28px; }
  .card--front .web-strip { position: absolute; left: 68px; top: 160px; }
  .details-box {
    position: absolute; left: 26px; top: 200px;
    width: 280px; height: 92px;
    background: var(--ink-dark);
    border: 3px solid var(--gold);
    color: var(--ink-text);
    text-align: center;
    font-size: 15px; line-height: 18px;
    padding: 8px 10px;
  }
  .details-box .rule { border-top: 1px solid var(--ink-text); margin: 4px 0 3px; }
  .window-frame { position: absolute; left: 326px; top: 26px; }
</style>
</head>
<body>

  <section class="card card--back" aria-label="Back of card">
    <div class="bevel-frame">
      <div class="room-view" role="img" aria-label="Softly blurred photograph of a bright home interior">
        <div class="mark">Casement Craft<br>Renewals</div>
        <div class="web-strip">www.casementcraftrenewals.com</div>
        <div class="contact-bar">
          Casement Craft Renewals Owen Castell 0457 302 689<br>
          owen@casementcraftrenewals.com
        </div>
      </div>
    </div>
  </section>

  <section class="card card--front" aria-label="Front of card">
    <div class="mark">Casement Craft<br>Renewals</div>
    <div class="web-strip">www.casementcraftrenewals.com</div>
    <div class="details-box">
      Casement Craft Renewals<br>
      Owen Castell 0457 302 689
      <div class="rule"></div>
      owen@casementcraftrenewals.com
    </div>
    <svg class="window-frame" width="196" height="262" viewBox="0 0 196 262">
      <defs>
        <linearGradient id="room-tones" x1="0" y1="0" x2="1" y2="1">
          <stop offset="0" stop-color="#efeeea"/>
          <stop offset="0.45" stop-color="#cdb58c"/>
          <stop offset="1" stop-color="#8f8a82"/>
        </linearGradient>
      </defs>
      <rect x="0" y="0" width="196" height="262" fill="#ffffff" stroke="#d5d5d3"/>
      <rect x="6" y="6" width="184" height="250" fill="none" stroke="#dcdcda"/>
      <g role="img" aria-label="Photograph of a modern kitchen and dining room seen through the window">
        <rect x="14" y="14" width="168" height="234" fill="url(#room-tones)"/>
      </g>
      <rect x="92" y="14" width="12" height="234" fill="#ffffff" stroke="#d5d5d3"/>
      <rect x="14" y="125" width="168" height="12" fill="#ffffff" stroke="#d5d5d3"/>
      <rect x="14" y="14" width="168" height="234" fill="none" stroke="#c9c9c7"/>
    </svg>
  </section>

</body>
</html>
```